Velora Aesthetica

Medical doctor providing aesthetic medicine

* Double sided card
* Logo to be on card
Other details:
* Dr. Mirela Kostvan, BSc, MBChB, CCFP
* #214-215, 27903 83 Ave, Surrey, BC, V2T 4K7
* 604-718-2943
* info@veloraclinic.ca
* www.veloraclinic.ca

Industry/Entity Type

Medical / Health & Beauty

Contact Information for Business Card

see 'Project Description'

Colors
0054AA
0677BA
7BADD7
CADEEF
E8F1F8
FFF300
FFF600
FEFA6F
FFFEC7
FFFEE8

Requirements
Must have
• Modern, high-end design

```html
<!DOCTYPE html>
<html lang="en">
<head>
<meta charset="utf-8">
<title>Velora Aesthetica – Business Card</title>
<link href="https://fonts.googleapis.com/css2?family=Montserrat:wght@500;600&family=Roboto:wght@400;500;700&display=swap" rel="stylesheet">
<style>
  :root {
    --page-bg: #2a2a2c;
    --card-dark-1: #1d2227;
    --card-dark-2: #2c3238;
    --navy: #1c3654;
    --gold: #e3b51c;
    --white: #ffffff;
    --text-soft: #d9dde2;
  }
  * { box-sizing: border-box; margin: 0; padding: 0; }
  html, body { width: 1200px; height: 852px; overflow: hidden; }
  body {
    background: var(--page-bg);
    font-family: "Roboto", Arial, sans-serif;
    position: relative;
  }
  .card {
    position: absolute;
    width: 540px;
    height: 309px;
    border-radius: 18px;
    overflow: hidden;
    top: 272px;
  }
  .card-front {
    left: 40px;
    background: linear-gradient(135deg, var(--card-dark-2), var(--card-dark-1));
    border-bottom: 5px solid var(--gold);
  }
  .card-back {
    left: 620px;
    background: linear-gradient(135deg, var(--card-dark-1), var(--card-dark-2));
  }
  .brand {
    position: absolute;
    text-align: center;
    font-family: "Montserrat", Arial, sans-serif;
    font-weight: 500;
    color: var(--white);
    text-transform: uppercase;
    line-height: 1.35;
  }
  .card-front .brand {
    left: 0; right: 0; top: 118px;
    font-size: 30px;
    letter-spacing: 10px;
  }
  .card-front .brand .brand-sub { font-size: 13px; letter-spacing: 7px; display: block; }
  .card-back .brand {
    left: 290px; width: 250px; top: 92px;
    font-size: 24px;
    letter-spacing: 7px;
  }
  .card-back .brand .brand-sub { font-size: 10px; letter-spacing: 5px; display: block; }
  .back-shape { position: absolute; inset: 0; }
  .doctor {
    position: absolute;
    left: 34px; top: 78px;
  }
  .doctor-name {
    color: var(--gold);
    font-weight: 700;
    font-size: 17px;
    white-space: nowrap;
  }
  .doctor-credentials {
    color: var(--text-soft);
    font-size: 11px;
    margin-top: 3px;
  }
  .contact-list {
    position: absolute;
    left: 34px; top: 176px;
    list-style: none;
    color: var(--text-soft);
    font-size: 11.5px;
    line-height: 19px;
  }
  .contact-list li { display: flex; align-items: center; gap: 10px; white-space: nowrap; }
  .contact-list svg { width: 11px; height: 11px; flex: none; }
  .contact-address { padding-left: 21px; margin-top: 6px; line-height: 17px; }
</style>
</head>
<body>

<section class="card card-front" aria-label="Card front">
  <div class="brand">Velora<span class="brand-sub">Aesthetica</span></div>
</section>

<section class="card card-back" aria-label="Card back">
  <svg class="back-shape" viewBox="0 0 540 309" aria-hidden="true">
    <circle cx="538" cy="-20" r="340" fill="var(--gold)"/>
    <circle cx="550" cy="-30" r="335" fill="var(--navy)"/>
  </svg>

  <div class="brand">Velora<span class="brand-sub">Aesthetica</span></div>

  <div class="doctor">
    <p class="doctor-name">Dr. Mirela Kostvan</p>
    <p class="doctor-credentials">BSc, MBChB, CCFP</p>
  </div>

  <ul class="contact-list">
    <li>
      <svg viewBox="0 0 12 12"><path fill="var(--gold)" d="M2 1h3l1 3-1.5 1a7 7 0 0 0 2.5 2.5L8 6l3 1v3a1 1 0 0 1-1 1A9 9 0 0 1 1 2a1 1 0 0 1 1-1z"/></svg>
      <span>604-718-2943</span>
    </li>
    <li>
      <svg viewBox="0 0 12 12"><rect x="1" y="2.5" width="10" height="7" fill="var(--gold)"/><path d="M1 2.5l5 4 5-4" stroke="var(--card-dark-1)" fill="none"/></svg>
      <span>info@veloraclinic.ca</span>
    </li>
    <li>
      <svg viewBox="0 0 12 12"><circle cx="6" cy="6" r="5" fill="var(--gold)"/><path d="M1 6h10M6 1c2 2.5 2 7.5 0 10M6 1c-2 2.5-2 7.5 0 10" stroke="var(--card-dark-1)" stroke-width=".8" fill="none"/></svg>
      <span>www.veloraclinic.ca</span>
    </li>
    <li class="contact-address">#214-215, 27903 83 Ave,<br>Surrey, BC, V2T 4K7</li>
  </ul>
</section>

</body>
</html>
```